Satchel & Compass needs new business card design

I need a new business card design. I'm looking for out-of-the-box design which represents the freedom of being a location independent entrepreneur.
I offer coaching, retreats and trips.
I would like to see designs with and without the photo.
Colors I use are black (#000000), green (#25A796) and brown (#D7C38C)
Website satchelandcompass.com

Target Market(s)

location independent entrepreneurs, digital nomads, people looking to swap the 9 to 5 for a lifestyle business

Industry/Entity Type

Business

Contact Information for Business Card

Petra Varga
Your Lifestyle Business Coach, Retreat & Trip Leader
http://satchelandcompass.com
hello@satchelandcompass.com
Live a life you don't need a holiday from

Font styles to use
Serif
Sans Serif

Requirements
Must have
• One side should contain only the logo. I would also consider having the "Live a life you don't need a holiday from" on that side too (depending on how it looks)
• Please show both sides on the designs.

```html
<!DOCTYPE html>
<html lang="en">
<head>
<meta charset="utf-8">
<title>Satchel &amp; Compass – Business Card</title>
<link rel="stylesheet" href="https://fonts.googleapis.com/css2?family=Open+Sans:wght@400;600;700&display=swap">
<style>
  :root {
    --ink: #1a1a1a;
    --card-dark: #231f20;
    --green: #25a796;
    --paper: #ffffff;
    --muted: #4a4a4a;
    --backdrop: #e6e6e6;
  }
  * { box-sizing: border-box; margin: 0; padding: 0; }
  html, body {
    width: 1105px;
    height: 1200px;
    overflow: hidden;
  }
  body {
    background: var(--backdrop);
    font-family: "Open Sans", Arial, sans-serif;
    position: relative;
  }
  .card {
    position: absolute;
    left: 196px;
    width: 720px;
    height: 412px;
    overflow: hidden;
  }
  .card--front { top: 146px; background: var(--paper); }
  .card--back  { top: 602px; background: var(--card-dark); }

  /* Front */
  .brand-name {
    position: absolute;
    left: 41px;
    top: 62px;
    font-size: 44px;
    font-weight: 700;
    color: var(--ink);
    letter-spacing: 0.5px;
    line-height: 1;
  }
  .contact-list {
    position: absolute;
    left: 41px;
    top: 312px;
    list-style: none;
  }
  .contact-list li {
    display: flex;
    align-items: center;
    gap: 10px;
    font-size: 19px;
    color: var(--muted);
    height: 28px;
  }
  .contact-icon { width: 17px; height: 17px; flex: none; }
  .person {
    position: absolute;
    right: 36px;
    top: 278px;
    text-align: right;
  }
  .person-name {
    font-size: 25px;
    font-weight: 600;
    color: var(--green);
    letter-spacing: 0.5px;
    line-height: 34px;
  }
  .person-role {
    font-size: 19px;
    color: var(--ink);
    line-height: 28px;
  }
  .edge-tab {
    position: absolute;
    right: 0;
    top: 283px;
    width: 17px;
    height: 79px;
    background: var(--card-dark);
  }

  /* Back */
  .social-links {
    position: absolute;
    top: 25px;
    right: 23px;
    display: flex;
    gap: 6px;
  }
  .social-links span {
    width: 27px;
    height: 26px;
    background: var(--green);
  }
  .brand-name--centered {
    position: absolute;
    left: 0;
    right: 0;
    top: 180px;
    text-align: center;
    font-size: 54px;
    font-weight: 700;
    color: var(--paper);
    letter-spacing: 1px;
    line-height: 1;
  }
  .tagline-band {
    position: absolute;
    left: 0;
    right: 0;
    top: 347px;
    height: 41px;
    background: var(--green);
    color: var(--paper);
    display: flex;
    align-items: center;
    justify-content: center;
    font-size: 19px;
    letter-spacing: 1px;
    text-transform: uppercase;
  }
</style>
</head>
<body>
  <section class="card card--front">
    <div class="brand-name">Satchel &amp; Compass</div>

    <ul class="contact-list">
      <li>
        <svg class="contact-icon" viewBox="0 0 16 16" aria-hidden="true">
          <rect x="1" y="3" width="14" height="10" fill="#25a796"/>
          <path d="M1 3 L8 9 L15 3" fill="none" stroke="#fff" stroke-width="1.4"/>
        </svg>
        hello@satchelandcompass.com
      </li>
      <li>
        <svg class="contact-icon" viewBox="0 0 16 16" aria-hidden="true">
          <circle cx="8" cy="8" r="7" fill="#25a796"/>
          <ellipse cx="8" cy="8" rx="3" ry="7" fill="none" stroke="#fff" stroke-width="1"/>
          <line x1="1" y1="8" x2="15" y2="8" stroke="#fff" stroke-width="1"/>
        </svg>
        www.satchelandcompass.com
      </li>
    </ul>

    <div class="person">
      <p class="person-name">PETRA VARGA</p>
      <p class="person-role">Your Lifestyle Business Coach</p>
      <p class="person-role">Retreat &amp; Trip Leader</p>
    </div>
    <div class="edge-tab"></div>
  </section>

  <section class="card card--back">
    <div class="social-links" aria-label="Social profiles">
      <span></span><span></span><span></span>
    </div>
    <div class="brand-name--centered">Satchel &amp; Compass</div>
    <div class="tagline-band">Live a life you don't need a holiday from</div>
  </section>
</body>
</html>
```